Ink & Toner Postcards (Set of 3)

Postcard
Some Content:

Header Option: STOP Killing your Printer with
Inferior Cartridges

Header Option: STOP Spending TOO MUCH $$ on Cheap Toner Cartridges

Secondary Message" Save Money
with QUALITY Toner Cartridges

Points to Get Across:
Buy Fewer Cartridges, Generate Over 25% (+) Yield
Eliminate Toner Contamination and Reduce Jams
Ensure Top Quality Printing and Printer Reliability
Competitive Prices

To Order, Visit qelvorink.com

Special Volume & Bundling Pricing
Call 877-412-5596

Target Market(s)

Small Business Owners
Independent Pharmacies

Industry/Entity Type

Printer

Requirements
Must have
• Phone Number
Website Address
2nd Side B&W, Set Up For Mailing
Output: Adobe Acrobat 9 Document (*.pdf) (recommended)
and
Adobe Illustrator CS3 Artwork (*.ai) (recommended)
or
Adobe Photoshop CS3 Image (*.psd) (recommended)

Full Bleed Size
5.59" x 4.33"
142 x 110 mm
1677 x 1300 pixels

Document Trim Size
5.47" x 4.21"
139 x 107 mm
1642 x 1264 pixels

OR

Full Bleed Size
8.64" x 5.59"
219 x 142 mm
2592 x 1677 pixels

Document Trim Size
8.52" x 5.47"
216 x 139 mm
2556 x 1642 pixels
Should not have
• Too Much Wording, Need Impact of Messaging To Act

```html
<!DOCTYPE html>
<html lang="en">
<head>
<meta charset="utf-8">
<title>Qelvor Ink – Toner Postcard</title>
<link href="https://fonts.googleapis.com/css2?family=Montserrat:ital,wght@0,400;0,500;0,600;0,700;1,400&display=swap" rel="stylesheet">
<style>
  :root {
    --stage: #272727;
    --green-deep: #0b6a2c;
    --green: #18933d;
    --green-bright: #2eab4a;
    --lime: #8fd14f;
    --navy: #1f3b8c;
    --ink: #333333;
    --white: #ffffff;
    --rule: #8a8a8a;
    --cartridge: #2f3233;
  }
  * { box-sizing: border-box; margin: 0; padding: 0; }
  html, body { width: 1200px; height: 576px; overflow: hidden; }
  body {
    background: var(--stage);
    font-family: "Montserrat", sans-serif;
    position: relative;
  }
  .card { position: absolute; overflow: hidden; }

  /* Front */
  .card-front {
    left: 36px; top: 45px; width: 556px; height: 387px;
    background: linear-gradient(160deg, var(--green-deep) 0%, var(--green) 55%, var(--green-bright) 100%);
    color: var(--white);
  }
  .headline {
    position: absolute; top: 28px; left: 0; width: 100%;
    text-align: center; font-weight: 700; font-size: 30px; line-height: 40px;
  }
  .headline .accent { color: var(--lime); }
  .save-title {
    position: absolute; left: 44px; top: 137px; font-size: 25px; font-weight: 700;
  }
  .save-sub {
    position: absolute; left: 39px; top: 170px; font-size: 10.5px; font-weight: 600;
  }
  .benefits {
    position: absolute; left: 229px; top: 137px; list-style: none;
    font-size: 11px; font-weight: 500; line-height: 14.5px;
  }
  .cartridge {
    position: absolute; background: linear-gradient(180deg, #4a4e50, var(--cartridge));
    border-radius: 6px;
  }
  .cartridge-1 { left: 8px; top: 218px; width: 100px; height: 46px; transform: rotate(6deg); }
  .cartridge-2 { left: 146px; top: 212px; width: 112px; height: 62px; transform: rotate(10deg); }
  .cartridge-3 { left: 288px; top: 262px; width: 106px; height: 42px; transform: rotate(14deg); }
  .cartridge-4 { left: 412px; top: 318px; width: 110px; height: 54px; transform: rotate(-6deg); }
  .wave { position: absolute; left: 0; top: 0; }
  .brand-name {
    position: absolute; font-weight: 700; color: var(--navy);
    display: flex; flex-direction: column; align-items: center; gap: 6px;
  }
  .brand-dot { width: 26px; height: 26px; border-radius: 50%; background: var(--navy); }
  .card-front .brand-name { left: 12px; top: 336px; font-size: 11px; }
  .contact { position: absolute; color: var(--ink); font-size: 9px; line-height: 11.5px; }
  .card-front .contact { left: 119px; top: 328px; }
  .contact .phone { color: var(--green); font-weight: 700; font-size: 15px; line-height: 18px; }
  .contact .order { font-style: italic; font-size: 11.5px; }

  /* Back */
  .card-back {
    left: 615px; top: 45px; width: 549px; height: 387px; background: var(--white);
  }
  .card-back .brand-name { left: 22px; top: 26px; font-size: 13px; align-items: flex-start; }
  .card-back .brand-dot { width: 40px; height: 40px; margin-left: 30px; }
  .card-back .contact { left: 22px; top: 121px; font-size: 9.5px; line-height: 12px; }
  .card-back .contact .phone { color: var(--navy); }
  .divider {
    position: absolute; left: 278px; top: 40px; width: 1px; height: 282px; background: var(--rule);
  }
  .stamp {
    position: absolute; left: 378px; top: 23px; width: 142px; height: 90px;
    background: linear-gradient(135deg, #e4e0e3, #b9a7c9 50%, #e8e4e6);
  }
  .address-lines { position: absolute; left: 302px; top: 224px; width: 208px; }
  .address-lines span { display: block; height: 1px; background: var(--rule); margin-bottom: 24px; }
  .shipping {
    position: absolute; left: 22px; top: 340px; color: var(--navy);
    font-weight: 700; font-size: 13.5px; line-height: 16px;
  }
</style>
</head>
<body>
  <section class="card card-front">
    <h1 class="headline">STOP Spending TOO MUCH $$<br>on <span class="accent">Cheap Toner Cartridges</span></h1>
    <h2 class="save-title">Save Money</h2>
    <p class="save-sub">with QUALITY Toner Cartridges</p>
    <ul class="benefits">
      <li>Buy Fewer Cartridges, Generate Over 25% (+) Yield</li>
      <li>Eliminate Toner Contamination and Reduce Jams</li>
      <li>Ensure Top Quality Printing and Printer Reliability</li>
      <li>Competitive Prices</li>
    </ul>
    <div class="cartridge cartridge-1" role="img" aria-label="Photo of a black toner cartridge"></div>
    <div class="cartridge cartridge-2" role="img" aria-label="Photo of a black toner cartridge"></div>
    <div class="cartridge cartridge-3" role="img" aria-label="Photo of a black toner cartridge"></div>
    <svg class="wave" width="556" height="387" viewBox="0 0 556 387">
      <path d="M0 288 C125 268 300 280 412 387 L395 387 C290 290 120 278 0 296 Z" fill="#1f3b8c"/>
      <path d="M0 296 C120 278 290 290 395 387 L0 387 Z" fill="#ffffff"/>
    </svg>
    <div class="cartridge cartridge-4" role="img" aria-label="Photo of a black toner cartridge"></div>
    <div class="brand-name"><span class="brand-dot"></span>Qelvor Ink, LLC.</div>
    <div class="contact">
      <p>Special Volume &amp; Bundling Pricing</p>
      <p class="phone">Call 877-412-5596</p>
      <p>Visit our website for more information and</p>
      <p><span class="order">To Order today!</span> Visit www.<strong>qelvorink</strong>.com</p>
    </div>
  </section>

  <section class="card card-back">
    <div class="brand-name"><span class="brand-dot"></span>Qelvor Ink, LLC.</div>
    <div class="contact">
      <p>Special Volume &amp; Bundling Pricing</p>
      <p class="phone">Call 877-412-5596</p>
      <p class="order">To Order today!</p>
      <p>Visit www.<strong>qelvorink</strong>.com</p>
    </div>
    <div class="divider"></div>
    <div class="stamp" role="img" aria-label="Postage stamp with cancellation marks"></div>
    <div class="address-lines"><span></span><span></span><span></span><span></span><span></span></div>
    <svg class="wave" width="549" height="387" viewBox="0 0 549 387">
      <path d="M0 285 C150 270 260 300 315 387 L0 387 Z" fill="#1f3b8c"/>
      <path d="M0 293 C140 280 245 308 298 387 L0 387 Z" fill="#18933d"/>
    </svg>
    <p class="shipping">Free Domestic Shipping<br>on all Orders over $95</p>
  </section>
</body>
</html>
```